Tidewell building company Business card design

I need a business card design for my company. I have a logo but dont have business cards with our logo..

www.tidewellbuildingco.com.au

The logo is on the website

I need the same details as this design I have attached. we have changed the logo and colours. just like the website

```html
<!DOCTYPE html>
<html lang="en">
<head>
<meta charset="utf-8">
<title>Tidewell Building – Business Card</title>
<link rel="stylesheet" href="https://fonts.googleapis.com/css2?family=Tinos&display=swap">
<style>
  :root {
    --page-bg: #ffffff;
    --card-bg: #ffffff;
    --brand-blue: #33a8f2;
    --brand-grey: #bdcbcc;
    --text-dark: #111111;
    --logo-dark: #2a2a2a;
  }
  html, body {
    margin: 0;
    padding: 0;
    width: 1200px;
    height: 1000px;
    overflow: hidden;
    background: var(--page-bg);
  }
  .canvas {
    position: relative;
    width: 1200px;
    height: 1000px;
    font-family: "Tinos", "Times New Roman", serif;
    color: var(--text-dark);
  }
  .card-shapes {
    position: absolute;
    left: 0;
    top: 0;
  }
  .brand {
    position: absolute;
    left: 118px;
    top: 300px;
    width: 200px;
    text-align: center;
    color: var(--brand-blue);
  }
  .brand-mark {
    display: block;
    width: 46px;
    height: 46px;
    margin: 0 auto 22px;
    background: var(--brand-blue);
  }
  .brand-name {
    display: block;
    font-size: 40px;
    line-height: 44px;
    letter-spacing: 1px;
  }
  .brand-sub {
    display: block;
    font-size: 22px;
    line-height: 26px;
    letter-spacing: 7px;
  }
  .contact-left {
    position: absolute;
    left: 120px;
    top: 519px;
    font-size: 23px;
    line-height: 31.6px;
  }
  .contact-left p { margin: 0; }
  .person {
    position: absolute;
    right: 125px;
    top: 560px;
    text-align: right;
    font-size: 23px;
    line-height: 33px;
  }
  .person p { margin: 0; }
  .person-name {
    display: inline-block;
    font-size: 38px;
    line-height: 44px;
    padding: 0 2px 0 10px;
    margin-right: -15px;
    margin-bottom: 18px;
    border-bottom: 2px solid var(--text-dark);
  }
</style>
</head>
<body>
<main class="canvas">
  <svg class="card-shapes" width="1200" height="1000" viewBox="0 0 1200 1000" aria-hidden="true">
    <rect class="card" x="68" y="205" width="1064" height="590" fill="var(--card-bg)"/>
    <path class="top-swoosh-edge" d="M68,205 C600,290 1000,430 1132,593 L1132,205 Z" fill="var(--brand-grey)"/>
    <path class="top-swoosh" d="M112,205 C620,285 1020,420 1132,565 L1132,205 Z" fill="var(--brand-blue)"/>
    <path class="bottom-swoosh-edge" d="M68,413 C200,560 600,700 1132,795 L68,795 Z" fill="var(--brand-blue)"/>
    <path class="bottom-swoosh" d="M68,445 C220,590 620,720 1080,795 L68,795 Z" fill="var(--brand-grey)"/>
  </svg>

  <div class="brand">
    <span class="brand-mark"></span>
    <span class="brand-name">TIDEWELL</span>
    <span class="brand-sub">BUILDING</span>
  </div>

  <section class="contact-left">
    <p>Address :</p>
    <p>Unit 1 Level 1,</p>
    <p>27 Marrick Ave,</p>
    <p>Pellham, WA 6031</p>
    <p>Email &nbsp;&nbsp;&nbsp;:</p>
    <p>info@tidewellbuildingco.com.au</p>
    <p>Web :</p>
    <p>www.tidewellbuildingco.com.au</p>
  </section>

  <section class="person">
    <span class="person-name">Name</span>
    <p>Phone :&nbsp;</p>
    <p>9417 2035</p>
    <p>Mob &nbsp;&nbsp;:&nbsp;</p>
    <p>0412558903 ( Mira )</p>
  </section>
</main>
</body>
</html>
```